International games company requires localisation design of gfa prediction game.

Using our current designs and those of our competitors, Brightwater Play are looking for novel design work that refreshes, enlivens and brings our games in line with what is expected in the American market. The Sports lottery game works by users selecting a winning margin for a series of 8 (in this case) GFA games. Should all of these predictions be correct, the user wins the jackpot.We are a software developer that creates free-to-play games specialised for the iGaming industry which function as customer acquisition and retention tools. Our user acquisition and retention models and processes are differentiated from our competitors by being driven by our unique style and application of gamification techniques and user behaviour analysis. Designs submitted should take inspiration from the attached images but designers should feel free to add their own flair and creativity whilst embracing intuitive UX and UI design principles.

Target Market(s)

American Sports fans aged 18+

Font styles to use
Sans Serif

Colors

Designer to choose colors to be used in the design.

Requirements
Must have
• User-friendly, intelligent design, applicable to being recoloured and branded to fit client's brands.

```html
<!DOCTYPE html>
<html lang="en">
<head>
<meta charset="utf-8">
<title>GFA Prediction Game – Screens</title>
<link href="https://fonts.googleapis.com/css2?family=Barlow:wght@400;500;600;700&display=swap" rel="stylesheet">
<style>
:root{
  --purple:#a23fd6;
  --purple-deep:#7b22b8;
  --purple-light:#d35ae8;
  --ink:#2b2b33;
  --muted:#8a8a95;
  --card:#ffffff;
  --tile:#f4f4f7;
  --page:#ffffff;
  --shadow:0 6px 18px rgba(60,20,90,.12);
}
*{box-sizing:border-box;margin:0;padding:0}
html,body{width:1024px;height:1200px;overflow:hidden;background:var(--page);font-family:"Barlow",Arial,sans-serif;color:var(--ink)}
.canvas{position:relative;width:1024px;height:1200px}
.screen{position:absolute;width:210px;height:442px;background:var(--card);border-radius:26px;overflow:hidden;box-shadow:0 10px 30px rgba(40,20,70,.13)}
.hdr{position:absolute;left:0;top:0;width:100%;background:linear-gradient(160deg,var(--purple-light),var(--purple) 55%,var(--purple-deep))}
.back{position:absolute;left:14px;top:30px;width:14px;height:12px}
.menu{position:absolute;right:16px;top:31px;width:18px;height:10px}
.abs{position:absolute}
.center{text-align:center}
/* list screen */
.league{position:absolute;left:15px;top:50px;color:#fff;font-size:19px;font-weight:600;letter-spacing:.5px;line-height:1}
.league-day{position:absolute;left:15px;top:70px;color:#f3dcff;font-size:7.5px;font-weight:500;letter-spacing:.4px}
.round-btn{position:absolute;top:56px;width:22px;height:22px;border-radius:50%;background:#fff;color:var(--purple);font-size:5px;font-weight:700;display:flex;align-items:center;justify-content:center;text-align:center;line-height:1}
.pick-card{position:absolute;left:15px;width:56px;height:48px;background:#fff;border-radius:4px;box-shadow:var(--shadow);border-top:2px solid var(--purple);border-right:2px solid var(--purple);text-align:center;font-size:7px;line-height:1.35;padding-top:20px}
.game-card{position:absolute;left:76px;width:118px;height:46px;background:#fff;border-radius:5px;box-shadow:var(--shadow)}
.crest{position:absolute;width:13px;height:13px;border-radius:50%}
.game-team{position:absolute;top:30px;width:44px;text-align:center;font-size:6.5px}
.score-box{position:absolute;left:46px;top:2px;width:21px;height:42px;border:1px solid #e4e4ea;border-radius:4px;text-align:center;font-size:6.5px;line-height:13px}
.score-box .final{color:var(--purple);font-size:5.5px}
.breakdown{position:absolute;left:5px;top:401px;width:200px;height:35px;border-radius:0 0 20px 20px;background:linear-gradient(90deg,var(--purple),var(--purple-deep));color:#fff;font-size:8px;font-weight:600;display:flex;align-items:center;justify-content:center;gap:4px}
/* pick screens */
.prompt{position:absolute;left:20px;right:20px;top:50px;color:#fff;font-size:9px;font-weight:600;line-height:14px;text-align:center}
.match-card{position:absolute;left:21px;top:101px;width:168px;height:130px;background:#fff;box-shadow:var(--shadow)}
.sponsor{position:absolute;left:86px;top:84px;width:48px;height:48px;border-radius:50%;background:#fff;box-shadow:var(--shadow);display:flex;align-items:center;justify-content:center;color:var(--purple-deep);font-size:6px;font-weight:700;text-align:center;line-height:1.1}
.city{position:absolute;top:148px;width:70px;text-align:center;font-size:5.5px;letter-spacing:.3px}
.team{position:absolute;top:155px;width:70px;text-align:center;font-size:9px;font-weight:700;letter-spacing:.3px}
.team-mark{position:absolute;top:180px;width:22px;height:22px;border-radius:50%}
.vs{position:absolute;width:22px;height:22px;border-radius:50%;background:radial-gradient(circle at 35% 35%,#c95bf0,var(--purple-deep));color:#fff;font-size:6.5px;display:flex;align-items:center;justify-content:center;box-shadow:0 3px 8px rgba(123,34,184,.35)}
.winby{position:absolute;top:212px;width:56px;height:44px;background:linear-gradient(160deg,#b84be0,var(--purple-deep));color:#fff;text-align:center;font-size:9.5px;line-height:15px;padding-top:6px;border-radius:0 0 4px 4px;box-shadow:var(--shadow)}
.winby small,.margin small{font-size:5px}
.margin-label{position:absolute;left:0;right:0;top:280px;text-align:center;font-size:7.5px;letter-spacing:.3px}
.margin{position:absolute;height:26px;display:flex;align-items:center;justify-content:center;font-size:9px;background:#fff;box-shadow:var(--shadow);border-radius:4px}
.margin.active{background:linear-gradient(160deg,#b84be0,var(--purple-deep));color:#fff;border-radius:4px 4px 0 0;z-index:2}
.answered{position:absolute;left:0;right:0;text-align:center;font-size:7.5px}
.dots{position:absolute;left:0;right:0;display:flex;justify-content:center;gap:1.5px}
.dots span{width:5px;height:5px;border-radius:50%;border:.7px solid #777}
.dots span.on{background:var(--purple);border-color:var(--purple)}
.home-bar{position:absolute;left:76px;top:429px;width:66px;height:2px;border-radius:2px;background:#111}
/* question screens */
.fixture{position:absolute;left:21px;top:52px;width:168px;height:57px;background:#fff;border-radius:0 0 6px 6px;box-shadow:var(--shadow)}
.fixture .name{position:absolute;top:14px;width:60px;text-align:center;font-size:7.5px;font-weight:600}
.fixture .mark{position:absolute;top:28px;width:22px;height:22px;border-radius:50%}
.kick-time{position:absolute;left:68px;top:27px;width:30px;height:8px;border-radius:4px;background:var(--purple);color:#fff;font-size:4.5px;display:flex;align-items:center;justify-content:center}
.question{position:absolute;left:14px;right:14px;text-align:center;font-size:7.5px;line-height:12px}
.group{position:absolute;left:21px;width:168px;background:#fff;border-radius:6px;box-shadow:var(--shadow)}
.group-mark{position:absolute;left:7px;width:44px;height:54px;background:var(--tile);border-radius:4px}
.group-mark i{position:absolute;left:10px;top:15px;width:24px;height:24px;border-radius:50%}
.choice{position:absolute;background:var(--tile);border-radius:6px;font-size:5.5px;line-height:8px;padding:5px 0 0 10px}
.choice .bar{display:inline-block;height:2px;border-radius:1px;background:var(--purple);vertical-align:middle;margin-left:2px}
.choice .radio{position:absolute;right:8px;top:9px;width:6px;height:6px;border-radius:50%;border:.7px solid #cfcfd6}
.choice.selected{background:linear-gradient(90deg,#c24fe0,var(--purple-deep));color:#fff;font-weight:600}
.choice.selected .bar{background:#fff}
.choice.selected .radio{border-color:#fff}
.letter{position:absolute;left:28px;width:28px;height:26px;background:var(--tile);border-radius:4px;color:var(--purple);font-size:9px;font-weight:600;display:flex;align-items:center;justify-content:center}
</style>
</head>
<body>
<div class="canvas">

<!-- ============ Screen 1: weekend list ============ -->
<section class="screen" style="left:77px;top:66px">
  <div class="hdr" style="height:172px;clip-path:polygon(0 0,100% 0,100% 140px,0 172px)"></div>
  <svg class="back" viewBox="0 0 14 12"><path d="M13 6H2M6 1 1 6l5 5" fill="none" stroke="#fff" stroke-width="1.4"/></svg>
  <svg class="menu" viewBox="0 0 18 10"><path d="M1 1h16M6 5h11M1 9h16" stroke="#fff" stroke-width="1.5" stroke-linecap="round"/></svg>
  <div class="league">CCSA</div>
  <div class="league-day">SATURDAY</div>
  <div class="round-btn" style="left:145px">KICK<br>LINE</div>
  <div class="round-btn" style="left:172px"><svg width="12" height="8" viewBox="0 0 12 8"><circle cx="3" cy="2.2" r="1.8" fill="#a23fd6"/><circle cx="9" cy="2.2" r="1.8" fill="#a23fd6"/><circle cx="6" cy="2.6" r="2" fill="#a23fd6"/><path d="M0 8a3 3 0 0 1 6 0M6 8a3 3 0 0 1 6 0M2.5 8a3.5 3.5 0 0 1 7 0" fill="#a23fd6"/></svg></div>

  <!-- row 1 -->
  <div class="pick-card" style="top:90px"><span class="crest" role="img" aria-label="Lakeview team crest" style="left:21px;top:5px;background:#c8202f"></span>Win By<br>7–9</div>
  <div class="game-card" style="top:97px">
    <span class="crest" role="img" aria-label="Lakeview team crest" style="left:15px;top:10px;background:#c8202f"></span>
    <div class="game-team" style="left:0">Lakeview</div>
    <div class="score-box">51<br><span class="final">Final</span><br>10</div>
    <span class="crest" role="img" aria-label="Ridgeway team crest" style="left:88px;top:10px;background:#9aa2b4"></span>
    <div class="game-team" style="left:73px">Ridgeway</div>
  </div>
  <!-- row 2 -->
  <div class="pick-card" style="top:166px"><span class="crest" role="img" aria-label="Keystone team crest" style="left:21px;top:5px;background:#1a2a5c"></span>Win By<br>7–9</div>
  <div class="game-card" style="top:174px">
    <span class="crest" role="img" aria-label="Ironport team crest" style="left:15px;top:10px;background:#222"></span>
    <div class="game-team" style="left:0">Ironport</div>
    <div class="score-box">51<br><span class="final">Final</span><br>10</div>
    <span class="crest" role="img" aria-label="Keystone team crest" style="left:88px;top:10px;background:#1a2a5c"></span>
    <div class="game-team" style="left:73px">Keystone</div>
  </div>
  <!-- row 3 -->
  <div class="pick-card" style="top:239px"><span class="crest" role="img" aria-label="Coastal team crest" style="left:21px;top:5px;background:#a3202c"></span>Win By<br>7–9</div>
  <div class="game-card" style="top:251px">
    <span class="crest" role="img" aria-label="Coastal team crest" style="left:15px;top:10px;background:#a3202c"></span>
    <div class="game-team" style="left:0">Coastal</div>
    <div class="score-box">51<br><span class="final">Final</span><br>10</div>
    <span class="crest" role="img" aria-label="Summit team crest" style="left:88px;top:10px;background:#c9a95a"></span>
    <div class="game-team" style="left:73px">Summit</div>
  </div>
  <!-- row 4 -->
  <div class="pick-card" style="top:314px"><span class="crest" role="img" aria-label="Gulfside team crest" style="left:21px;top:5px;background:#3b3320"></span>Win By<br>7–9</div>
  <div class="game-card" style="top:328px">
    <span class="crest" role="img" aria-label="Gulfside team crest" style="left:15px;top:10px;background:#3b3320"></span>
    <div class="game-team" style="left:0">Gulfside</div>
    <div class="score-box">51<br><span class="final">Final</span><br>10</div>
    <span class="crest" role="img" aria-label="Bluegrass team crest" style="left:88px;top:10px;background:#1f4fa8"></span>
    <div class="game-team" style="left:73px">Bluegrass</div>
  </div>

  <div class="breakdown"><svg width="12" height="8" viewBox="0 0 12 8"><path d="M1 4c2-3.5 8-3.5 10 0-2 3.5-8 3.5-10 0z" fill="none" stroke="#fff" stroke-width="1.2"/><circle cx="6" cy="4" r="1.6" fill="#fff"/></svg>View Breakdown</div>
</section>

<!-- ============ Screen 2: winning margin (Bayside) ============ -->
<section class="screen" style="left:406px;top:66px">
  <div class="hdr" style="height:178px;clip-path:polygon(0 0,100% 0,100% 145px,0 178px)"></div>
  <svg class="back" viewBox="0 0 14 12"><path d="M13 6H2M6 1 1 6l5 5" fill="none" stroke="#fff" stroke-width="1.4"/></svg>
  <svg class="menu" viewBox="0 0 18 10"><path d="M1 1h16M6 5h11M1 9h16" stroke="#fff" stroke-width="1.5" stroke-linecap="round"/></svg>
  <div class="prompt">Pick the team to win and by how many points</div>
  <div class="match-card"></div>
  <div class="sponsor">KICKLINE<br>SIX</div>
  <div class="city" style="left:21px">NORTHLAND</div>
  <div class="team" style="left:21px">MOOSE</div>
  <div class="city" style="left:119px">BAYSIDE</div>
  <div class="team" style="left:119px">HAULERS</div>
  <span class="team-mark" role="img" aria-label="Northland team mark" style="left:45px;background:#6b3fa0"></span>
  <div class="vs" style="left:94px;top:183px">VS</div>
  <span class="team-mark" role="img" aria-label="Bayside team mark" style="left:143px;background:#2f5a3a"></span>
  <div class="winby" style="left:124px">Win By<br>7 <small>to</small> 9</div>
  <div class="margin-label">HAULERS WIN BY</div>
  <div class="margin" style="left:14px;top:307px;width:68px">10 <small>&nbsp;to&nbsp;</small> 14</div>
  <div class="margin active" style="left:68px;top:299px;width:72px">7 <small>&nbsp;to&nbsp;</small> 9</div>
  <div class="margin" style="left:126px;top:307px;width:70px">5 <small>&nbsp;to&nbsp;</small> 6</div>
  <div class="answered" style="top:365px">1 of 6 answered</div>
  <div class="dots" style="top:380px"><span class="on"></span><span></span><span></span><span></span><span></span><span></span></div>
  <div class="home-bar"></div>
</section>

<!-- ============ Screen 3: margin bands ============ -->
<section class="screen" style="left:735px;top:66px">
  <div class="hdr" style="height:112px;clip-path:polygon(0 0,100% 0,100% 92px,0 112px)"></div>
  <svg class="back" viewBox="0 0 14 12"><path d="M13 6H2M6 1 1 6l5 5" fill="none" stroke="#fff" stroke-width="1.4"/></svg>
  <svg class="menu" viewBox="0 0 18 10"><path d="M1 1h16M6 5h11M1 9h16" stroke="#fff" stroke-width="1.5" stroke-linecap="round"/></svg>
  <div class="fixture">
    <div class="name" style="left:2px">COLOSSI</div>
    <div class="name" style="left:106px;top:12px">OCELOTS</div>
    <span class="mark" role="img" aria-label="Colossi team mark" style="left:22px;background:#2a5aa6"></span>
    <span class="mark" role="img" aria-label="Ocelots team mark" style="left:125px;background:#b98a2e"></span>
    <div class="vs" style="left:75px;top:8px;width:14px;height:14px;font-size:4.5px">VS</div>
    <div class="kick-time">06:00 PM</div>
  </div>
  <div class="question" style="top:122px">Which team will win in how many points?</div>
  <div class="group" style="top:143px;height:116px">
    <div class="group-mark" style="top:32px"><i role="img" aria-label="Colossi team mark" style="background:#2a5aa6"></i></div>
    <div class="choice" style="left:57px;top:6px;width:92px;height:26px">Colossi by 15+ pts<br>8%<span class="bar" style="width:10px"></span><span class="radio"></span></div>
    <div class="choice" style="left:57px;top:44px;width:92px;height:26px">Colossi by 7–14+ pts<br>46%<span class="bar" style="width:22px"></span><span class="radio"></span></div>
    <div class="choice" style="left:57px;top:83px;width:92px;height:26px">Colossi by 6 or less/tie<br>28%<span class="bar" style="width:14px"></span><span class="radio"></span></div>
  </div>
  <div class="group" style="top:267px;height:114px">
    <div class="group-mark" style="top:32px"><i role="img" aria-label="Ocelots team mark" style="background:#b98a2e"></i></div>
    <div class="choice" style="left:57px;top:6px;width:92px;height:26px">Ocelots by 6 or less/tie<br>12%<span class="bar" style="width:11px"></span><span class="radio"></span></div>
    <div class="choice" style="left:57px;top:45px;width:92px;height:26px">Ocelots by 7–14 pts<br>6%<span class="bar" style="width:7px"></span><span class="radio"></span></div>
    <div class="choice" style="left:57px;top:84px;width:92px;height:26px">Ocelots by 15+ pts<br>0%<span class="bar" style="width:2px"></span><span class="radio"></span></div>
  </div>
  <div class="answered" style="top:396px">1 of 6 answered</div>
  <div class="dots" style="top:411px"><span class="on"></span><span></span><span></span><span></span><span></span><span></span></div>
  <div class="home-bar"></div>
</section>

<!-- ============ Screen 4: multiple choice ============ -->
<section class="screen" style="left:241px;top:644px">
  <div class="hdr" style="height:112px;clip-path:polygon(0 0,100% 0,100% 92px,0 112px)"></div>
  <svg class="back" viewBox="0 0 14 12"><path d="M13 6H2M6 1 1 6l5 5" fill="none" stroke="#fff" stroke-width="1.4"/></svg>
  <svg class="menu" viewBox="0 0 18 10"><path d="M1 1h16M6 5h11M1 9h16" stroke="#fff" stroke-width="1.5" stroke-linecap="round"/></svg>
  <div class="fixture">
    <div class="name" style="left:2px">COLOSSI</div>
    <div class="name" style="left:106px;top:12px">OCELOTS</div>
    <span class="mark" role="img" aria-label="Colossi team mark" style="left:22px;background:#2a5aa6"></span>
    <span class="mark" role="img" aria-label="Ocelots team mark" style="left:125px;background:#b98a2e"></span>
    <div class="vs" style="left:75px;top:8px;width:14px;height:14px;font-size:4.5px">VS</div>
    <div class="kick-time">06:00 PM</div>
  </div>
  <div class="question" style="top:122px">What will be the longest field goal made in the first half?</div>
  <div class="group" style="left:11px;top:150px;width:188px;height:244px"></div>
  <div class="letter" style="top:160px">A</div>
  <div class="choice" style="left:61px;top:160px;width:122px;height:26px">1–29 yards<br>5%<span class="bar" style="width:7px"></span><span class="radio"></span></div>
  <div class="letter" style="top:198px">B</div>
  <div class="choice" style="left:61px;top:198px;width:122px;height:26px">30–39 yards<br>34%<span class="bar" style="width:18px"></span><span class="radio"></span></div>
  <div class="letter" style="top:237px">C</div>
  <div class="choice" style="left:61px;top:237px;width:122px;height:26px">40–44 yards<br>36%<span class="bar" style="width:20px"></span><span class="radio"></span></div>
  <div class="letter" style="top:275px">D</div>
  <div class="choice selected" style="left:61px;top:275px;width:122px;height:26px">45–49 yards<br>19%<span class="bar" style="width:14px"></span><span class="radio"></span></div>
  <div class="letter" style="top:313px">E</div>
  <div class="choice" style="left:61px;top:313px;width:122px;height:26px">No field goals made<br>4%<span class="bar" style="width:6px"></span><span class="radio"></span></div>
  <div class="letter" style="top:352px">F</div>
  <div class="choice" style="left:61px;top:352px;width:122px;height:26px">Colossi by 15+ pts<br>2%<span class="bar" style="width:4px"></span><span class="radio"></span></div>
  <div class="answered" style="top:400px">1 of 6 answered</div>
  <div class="dots" style="top:414px"><span class="on"></span><span></span><span></span><span></span><span></span><span></span></div>
  <div class="home-bar"></div>
</section>

<!-- ============ Screen 5: winning margin (Prairie) ============ -->
<section class="screen" style="left:571px;top:644px">
  <div class="hdr" style="height:178px;clip-path:polygon(0 0,100% 0,100% 145px,0 178px)"></div>
  <svg class="back" viewBox="0 0 14 12"><path d="M13 6H2M6 1 1 6l5 5" fill="none" stroke="#fff" stroke-width="1.4"/></svg>
  <svg class="menu" viewBox="0 0 18 10"><path d="M1 1h16M6 5h11M1 9h16" stroke="#fff" stroke-width="1.5" stroke-linecap="round"/></svg>
  <div class="prompt">Pick the team to win and by how many points</div>
  <div class="match-card"></div>
  <div class="sponsor">KICKLINE<br>SIX</div>
  <div class="city" style="left:21px">PRAIRIE</div>
  <div class="team" style="left:21px">RANCHERS</div>
  <div class="city" style="left:119px">CAPITOL</div>
  <div class="team" style="left:119px">SENTINELS</div>
  <span class="team-mark" role="img" aria-label="Prairie team mark" style="left:45px;background:#1d2f55"></span>
  <div class="vs" style="left:94px;top:183px">VS</div>
  <span class="team-mark" role="img" aria-label="Capitol team mark" style="left:143px;background:#7a1f2a"></span>
  <div class="winby" style="left:33px">Win By<br>7 <small>to</small> 9</div>
  <div class="margin-label">RANCHERS WIN BY</div>
  <div class="margin" style="left:14px;top:307px;width:68px">10 <small>&nbsp;to&nbsp;</small> 14</div>
  <div class="margin active" style="left:68px;top:299px;width:72px">7 <small>&nbsp;to&nbsp;</small> 9</div>
  <div class="margin" style="left:126px;top:307px;width:70px">5 <small>&nbsp;to&nbsp;</small> 6</div>
  <div class="answered" style="top:365px">1 of 6 answered</div>
  <div class="dots" style="top:380px"><span class="on"></span><span></span><span></span><span></span><span></span><span></span></div>
  <div class="home-bar"></div>
</section>

</div>
</body>
</html>
```